Marrowind Labs - pioneers of next generation consulting!

We are a next generation management consulting firm with two focus areas and USPs (unique selling points):>Technology driven business developmentWe are not developers, we are experts in HOW to apply and incorporate technology in your business dna to drive business growth and value-added change.>Creating high performing teams levering our philosophy of collective intelligence. We truly understand the need of human engagement and we know that the only way of getting there is by building strong relationships among people, a warm and open culture is a stepping stone towards effective collaboration within/among teams. - We don't want a ”corporate feel” to our templates. The organic feeling we have with our blue-on-blue blobs has the idea of ever changing movement and shape changing. Please see our website, www.marrowindlabs.se. - In our context we sit among classic business mgmt. consultants and classic IT mgmt. consultants. We cater to business, tech and humans as the ultimate vehicle of change and business value. -To have a clean template one suggestion is to only use blue, white and black and keeping other colors separate, as an alternative but we are truly open allow your creativity add value to this. We are looking to find a slide deck which we can pick slides from, depending on what/whom/why we interact with customer we want to create different outcomes and our presentations should support this.

Industry/Entity Type

Management Consulting

Requirements
Must have
• next generation powerpoint and how to package storytelling. please keep to our look and feel, we just arrived at our logo, colours and shapes. Help us to carry it into our ppt's as well.
Should not have
• Hi all, please have a look at our website. It is still very new and more will be done, but our goal is to make powerpoint to come alive again and mirror our pioneering hearts and brains.

```html
<!DOCTYPE html>
<html lang="en">
<head>
<meta charset="utf-8">
<title>Marrowind Labs – Slide Deck</title>
<link rel="stylesheet" href="https://fonts.googleapis.com/css2?family=Montserrat:wght@400;500;600;700&family=Oswald:wght@700&display=swap">
<style>
  :root{
    --blue:#2b6fd6;
    --blue-mid:#1f58b8;
    --blue-deep:#1b4798;
    --navy:#173a78;
    --white:#ffffff;
    --ink:#222831;
    --grey-text:#8a8f98;
    --card:#eef0f3;
    --stage-top:#f4f4f4;
    --stage-bottom:#c3c3c3;
  }
  *{box-sizing:border-box;margin:0;padding:0}
  html,body{width:740px;height:1200px;overflow:hidden}
  body{position:relative;font-family:"Montserrat",Arial,sans-serif;color:var(--ink);background:var(--stage-top)}
  .stage-top{position:absolute;left:0;top:0;width:740px;height:496px;background:var(--stage-top)}
  .stage-bottom{position:absolute;left:0;top:496px;width:740px;height:704px;background:var(--stage-bottom)}

  .slide{position:absolute;width:336px;height:190px;overflow:hidden;background:var(--white);box-shadow:0 8px 14px rgba(0,0,0,.22)}
  .slide svg.shapes{position:absolute;left:0;top:0;width:336px;height:190px}
  .cover-large{left:90px;top:90px;transform:scale(1.6667);transform-origin:0 0}
  .s1{left:22px;top:532px}.s2{left:382px;top:532px}
  .s3{left:22px;top:752px}.s4{left:382px;top:752px}
  .s5{left:22px;top:970px}

  .cover{background:var(--blue)}
  .cover .wordmark{position:absolute;left:0;right:0;top:73px;text-align:center;color:var(--white);font-weight:500;font-size:25px;letter-spacing:1px;text-transform:uppercase;white-space:nowrap}
  .url-pill{position:absolute;left:50%;top:109px;transform:translateX(-50%);background:var(--white);color:var(--navy);font-size:7px;font-weight:700;letter-spacing:1.6px;padding:3px 11px;border-radius:8px;white-space:nowrap}

  .brand-small{position:absolute;right:12px;top:12px;font-size:7.5px;font-weight:500;color:var(--navy);letter-spacing:.3px;text-transform:uppercase;white-space:nowrap}
  .footer-url{position:absolute;left:14px;bottom:8px;font-size:4.5px;letter-spacing:1.4px;color:var(--grey-text)}
  .page-no{position:absolute;right:6px;bottom:6px;font-size:5px;color:var(--white);font-weight:600}

  .toc-title{position:absolute;left:10px;top:78px;color:var(--white);font-family:"Oswald",Impact,sans-serif;font-weight:700;font-size:17px;line-height:1.2}
  .toc-list{position:absolute;left:146px;top:32px;list-style:none}
  .toc-list li{display:flex;align-items:center;height:17.7px;font-size:5px}
  .toc-num{width:20px;color:var(--ink)}
  .toc-dot{width:5px;height:5px;border-radius:50%;background:#9aa0a8;margin-right:12px;position:relative;z-index:1}
  .toc-line{position:absolute;left:168px;top:40px;width:1px;height:126px;background:#c9ccd1}

  .tab-title{position:absolute;left:10px;top:11px;color:var(--white);font-family:"Oswald",Impact,sans-serif;font-weight:700;font-size:10px;letter-spacing:.2px;white-space:nowrap}

  .photo{position:absolute;top:58px;height:96px}
  .photo-team{left:10px;width:104px;background:linear-gradient(135deg,#6d7a7c,#3e4a4f 55%,#8c8a7e)}
  .photo-desk{left:223px;width:104px;background:linear-gradient(135deg,#8a8c86,#4f5a62 50%,#b0a596)}
  .info-box{position:absolute;left:117px;top:58px;width:102px;height:96px;background:var(--navy);color:var(--white);text-align:center;padding:8px 7px}
  .info-box h3{font-size:7px;font-weight:600;margin-bottom:5px;letter-spacing:.3px}
  .info-box p{font-size:3.6px;line-height:1.55;margin-bottom:4px}

  .card{position:absolute;top:49px;width:60px;height:113px;background:var(--card);border-bottom:2px solid var(--navy);overflow:hidden}
  .card svg{position:absolute;left:0;top:0;width:60px;height:60px}
  .card-head{position:absolute;left:0;top:0;width:60px;height:10px;display:flex;align-items:center;gap:9px;padding-left:4px;color:var(--white);font-size:3.8px;font-weight:700;white-space:nowrap}
  .card p{position:absolute;left:6px;right:6px;top:68px;font-size:3.6px;line-height:1.55;text-align:center;color:#4a4f57}

  .callout{position:absolute;width:70px;font-size:3.6px;line-height:1.45;color:#4a4f57}
  .callout h4{font-size:4.6px;font-weight:700;color:var(--blue);margin-bottom:1px}
  .callout.right-align{text-align:right}
  .co-1{left:56px;top:41px}.co-2{left:206px;top:41px}
  .co-3{left:26px;top:87px}.co-4{left:241px;top:87px}

  .brand-large{position:absolute;left:400px;top:1048px;width:320px;text-align:center;font-size:25px;font-weight:500;color:var(--navy);letter-spacing:1px;text-transform:uppercase;white-space:nowrap}
</style>
</head>
<body>
  <div class="stage-top"></div>
  <div class="stage-bottom"></div>

  <!-- Hero cover slide -->
  <section class="slide cover cover-large">
    <svg class="shapes" viewBox="0 0 336 190" aria-hidden="true">
      <path d="M0 0H72C84 18 66 42 42 46C22 50 6 42 0 36Z" fill="#1f58b8"/>
      <path d="M0 0H50C56 14 42 28 24 30C12 31 4 26 0 22Z" fill="#1b4798"/>
      <path d="M336 82C306 86 288 110 296 134C304 156 282 172 266 190H336Z" fill="#1f58b8"/>
      <path d="M336 108C314 112 306 134 314 152C322 168 302 180 294 190H336Z" fill="#1b4798"/>
      <path d="M336 140C322 144 318 160 324 172C328 180 320 186 316 190H336Z" fill="#173a78"/>
    </svg>
    <div class="wordmark">Marrowind Labs</div>
    <div class="url-pill">www.marrowindlabs.se</div>
  </section>

  <!-- Slide 1: cover -->
  <section class="slide cover s1">
    <svg class="shapes" viewBox="0 0 336 190" aria-hidden="true">
      <path d="M0 0H72C84 18 66 42 42 46C22 50 6 42 0 36Z" fill="#1f58b8"/>
      <path d="M0 0H50C56 14 42 28 24 30C12 31 4 26 0 22Z" fill="#1b4798"/>
      <path d="M336 82C306 86 288 110 296 134C304 156 282 172 266 190H336Z" fill="#1f58b8"/>
      <path d="M336 108C314 112 306 134 314 152C322 168 302 180 294 190H336Z" fill="#1b4798"/>
      <path d="M336 140C322 144 318 160 324 172C328 180 320 186 316 190H336Z" fill="#173a78"/>
    </svg>
    <div class="wordmark">Marrowind Labs</div>
    <div class="url-pill">www.marrowindlabs.se</div>
  </section>

  <!-- Slide 2: table of content -->
  <section class="slide s2">
    <svg class="shapes" viewBox="0 0 336 190" aria-hidden="true">
      <path d="M0 0H72C94 30 80 62 94 92C108 124 100 160 78 190H0Z" fill="#1b4798"/>
      <path d="M336 22C326 40 312 48 300 62C286 78 296 92 290 104C282 120 298 136 316 138C326 139 332 144 336 150Z" fill="#1f58b8"/>
      <path d="M336 52C322 64 310 80 318 98C324 112 312 124 322 134C328 140 334 142 336 144Z" fill="#2b6fd6"/>
      <path d="M336 164C324 166 314 176 312 190H336Z" fill="#173a78"/>
    </svg>
    <div class="brand-small">Marrowind Labs</div>
    <h2 class="toc-title">TABLE OF<br>CONTENT</h2>
    <div class="toc-line"></div>
    <ul class="toc-list">
      <li><span class="toc-num">3</span><span class="toc-dot"></span>Add Your Title One</li>
      <li><span class="toc-num">4</span><span class="toc-dot"></span>Add Your Title Two</li>
      <li><span class="toc-num">5</span><span class="toc-dot"></span>Add Your Title Three</li>
      <li><span class="toc-num">6</span><span class="toc-dot"></span>Add Your Title Four</li>
      <li><span class="toc-num">7</span><span class="toc-dot"></span>Add Your Title Five</li>
      <li><span class="toc-num">8</span><span class="toc-dot"></span>Add Your Title Six</li>
      <li><span class="toc-num">9</span><span class="toc-dot"></span>Add Your Title Seven</li>
      <li><span class="toc-num">10</span><span class="toc-dot"></span>Add Your Title Eight</li>
    </ul>
    <div class="footer-url">www.marrowindlabs.se</div>
    <div class="page-no">2</div>
  </section>

  <!-- Slide 3 -->
  <section class="slide s3">
    <svg class="shapes" viewBox="0 0 336 190" aria-hidden="true">
      <path d="M0 0H134C124 22 108 36 80 40C50 44 20 44 0 48Z" fill="#2b6fd6"/>
      <path d="M0 0H124C116 18 100 30 72 34C44 38 18 38 0 40Z" fill="#173a78"/>
      <path d="M336 164C324 166 314 176 312 190H336Z" fill="#173a78"/>
    </svg>
    <h2 class="tab-title">ADD YOUR TITLE ONE</h2>
    <div class="brand-small">Marrowind Labs</div>
    <div class="photo photo-team" role="img" aria-label="Photo of a small team gathered around a laptop in a bright office"></div>
    <div class="info-box">
      <h3>HEADING HERE</h3>
      <p>We shape teams and technology into lasting growth. Every change starts with people who trust each other and share a clear goal.</p>
      <p>Open culture turns collective intelligence into real value for every client we serve.</p>
    </div>
    <div class="photo photo-desk" role="img" aria-label="Photo of a consultant working at a desk with a laptop"></div>
    <div class="footer-url">www.marrowindlabs.se</div>
    <div class="page-no">3</div>
  </section>

  <!-- Slide 4 -->
  <section class="slide s4">
    <svg class="shapes" viewBox="0 0 336 190" aria-hidden="true">
      <path d="M0 0H134C124 22 108 36 80 40C50 44 20 44 0 48Z" fill="#2b6fd6"/>
      <path d="M0 0H124C116 18 100 30 72 34C44 38 18 38 0 40Z" fill="#173a78"/>
      <path d="M336 164C324 166 314 176 312 190H336Z" fill="#173a78"/>
    </svg>
    <h2 class="tab-title">ADD YOUR TITLE TWO</h2>
    <div class="brand-small">Marrowind Labs</div>

    <div class="card" style="left:20px">
      <svg viewBox="0 0 60 60" aria-hidden="true">
        <path d="M0 0H60V10L0 58Z" fill="#2b6fd6"/><path d="M0 0H60L50 10H0Z" fill="#173a78"/>
        <circle cx="17" cy="30" r="3.2" fill="#fff"/><path d="M11 40C11 35 23 35 23 40Z" fill="#fff"/>
      </svg>
      <div class="card-head"><span>01</span><span>HEADING HERE</span></div>
      <p>Short text about this step and the value it brings to you.</p>
    </div>
    <div class="card" style="left:98px">
      <svg viewBox="0 0 60 60" aria-hidden="true">
        <path d="M0 0H60V10L0 58Z" fill="#2b6fd6"/><path d="M0 0H60L50 10H0Z" fill="#173a78"/>
        <circle cx="17" cy="30" r="4.5" fill="none" stroke="#fff" stroke-width="1.4"/><rect x="15" y="36" width="4" height="3" fill="#fff"/>
      </svg>
      <div class="card-head"><span>01</span><span>HEADING HERE</span></div>
      <p>Short text about this step and the value it brings to you.</p>
    </div>
    <div class="card" style="left:175px">
      <svg viewBox="0 0 60 60" aria-hidden="true">
        <path d="M0 0H60V10L0 58Z" fill="#2b6fd6"/><path d="M0 0H60L50 10H0Z" fill="#173a78"/>
        <rect x="10" y="33" width="3" height="6" fill="#fff"/><rect x="15" y="29" width="3" height="10" fill="#fff"/><rect x="20" y="25" width="3" height="14" fill="#fff"/>
      </svg>
      <div class="card-head"><span>01</span><span>HEADING HERE</span></div>
      <p>Short text about this step and the value it brings to you.</p>
    </div>
    <div class="card" style="left:254px">
      <svg viewBox="0 0 60 60" aria-hidden="true">
        <path d="M0 0H60V10L0 58Z" fill="#2b6fd6"/><path d="M0 0H60L50 10H0Z" fill="#173a78"/>
        <circle cx="13" cy="34" r="3" fill="none" stroke="#fff" stroke-width="1.2"/><circle cx="21" cy="34" r="3" fill="none" stroke="#fff" stroke-width="1.2"/><path d="M10 26H22V29H10Z" fill="#fff"/>
      </svg>
      <div class="card-head"><span>01</span><span>HEADING HERE</span></div>
      <p>Short text about this step and the value it brings to you.</p>
    </div>
    <div class="footer-url">www.marrowindlabs.se</div>
    <div class="page-no">4</div>
  </section>

  <!-- Slide 5 -->
  <section class="slide s5">
    <svg class="shapes" viewBox="0 0 336 190" aria-hidden="true">
      <path d="M0 0H134C124 22 108 36 80 40C50 44 20 44 0 48Z" fill="#2b6fd6"/>
      <path d="M0 0H124C116 18 100 30 72 34C44 38 18 38 0 40Z" fill="#173a78"/>
      <path d="M336 164C324 166 314 176 312 190H336Z" fill="#173a78"/>

      <g fill="none" stroke="#9aa0a8" stroke-width=".6">
        <path d="M128 46H140V115"/>
        <path d="M204 46H190V100"/>
        <path d="M98 92H104V140"/>
        <path d="M239 92H232V140"/>
      </g>
      <g stroke="#fff" stroke-width="1.5">
        <path d="M98 166A68 68 0 0 1 117.9 117.9L140.5 140.5A36 36 0 0 0 130 166Z" fill="#c8c8c8"/>
        <path d="M117.9 117.9A68 68 0 0 1 166 98V130A36 36 0 0 0 140.5 140.5Z" fill="#9a9a9a"/>
        <path d="M166 98A68 68 0 0 1 214.1 117.9L191.5 140.5A36 36 0 0 0 166 130Z" fill="#7a7a7a"/>
        <path d="M214.1 117.9A68 68 0 0 1 234 166H202A36 36 0 0 0 191.5 140.5Z" fill="#5a5a5a"/>
      </g>
      <path d="M134 166A32 32 0 0 1 198 166Z" fill="#2b6fd6"/>
      <g fill="#fff">
        <circle cx="122" cy="149" r="2.4"/><path d="M117 157C117 152 127 152 127 157Z"/>
        <circle cx="146" cy="119" r="3.6" fill="none" stroke="#fff" stroke-width="1"/><rect x="144.5" y="124" width="3" height="2"/>
        <rect x="181" y="121" width="2.4" height="5"/><rect x="184.8" y="118" width="2.4" height="8"/><rect x="188.6" y="115" width="2.4" height="11"/>
        <circle cx="208" cy="149" r="2.6" fill="none" stroke="#fff" stroke-width="1"/><circle cx="214" cy="149" r="2.6" fill="none" stroke="#fff" stroke-width="1"/>
      </g>
    </svg>
    <h2 class="tab-title">ADD YOUR TITLE THREE</h2>
    <div class="brand-small">Marrowind Labs</div>
    <div class="callout right-align co-1"><h4>HEADING HERE</h4>Short note on this part of the model.</div>
    <div class="callout co-2"><h4>HEADING HERE</h4>Short note on this part of the model.</div>
    <div class="callout right-align co-3"><h4>HEADING HERE</h4>Short note on this part of the model.</div>
    <div class="callout co-4"><h4>HEADING HERE</h4>Short note on this part of the model.</div>
    <div class="footer-url">www.marrowindlabs.se</div>
    <div class="page-no">5</div>
  </section>

  <div class="brand-large">Marrowind Labs</div>
</body>
</html>
```